Design a whitepaper for MARINE TELEMEDICINE SYSTEM

Hi - I would like the attached word document designing into an attractive and engaging white paper to promote the use of telemedicine to the marine industry.

Please read the copy and make the graphics and design fit. Also attaches are our design guidelines.

Target Market(s)

Marine

Industry/Entity Type

Marine

Font styles to use
Sans Serif
Other font styles liked:
• Calibri

Requirements
Must have
• Sorvind Nautic Logo and branding applied (www.sorvind-nautic.example) branding guidelines to follow
• Be engaging and attractive
• Have a great front cover
• images that match the copy
Nice to have
• Marine and medical related imagery
Should not have
• too much text on one page

```html
<!DOCTYPE html>
<html lang="en">
<head>
<meta charset="utf-8">
<title>Telemedicine for the Marine Industry – Whitepaper Cover Spread</title>
<link href="https://fonts.googleapis.com/css2?family=Open+Sans:wght@300;400;600;700&display=swap" rel="stylesheet">
<style>
  :root {
    --bg: #2b2b2d;
    --blue-mid: #3f7fbb;
    --blue-deep: #2d6aa3;
    --blue-light: #5d9fe0;
    --navy: #13233a;
    --white: #ffffff;
    --text-soft: rgba(255,255,255,0.88);
    --logo-blue: #1f5fae;
  }
  * { box-sizing: border-box; margin: 0; padding: 0; }
  html, body { width: 1200px; height: 789px; overflow: hidden; background: var(--bg); }
  body { font-family: "Open Sans", Arial, sans-serif; color: var(--white); }

  .spread { position: absolute; left: 42px; top: 0; width: 1116px; height: 789px; display: flex; }
  .page { position: relative; width: 558px; height: 789px; overflow: hidden; }
  .icon { display: block; flex: none; }

  /* Back cover */
  .back-cover { background: linear-gradient(160deg, #4b8cc6 0%, var(--blue-mid) 45%, var(--blue-deep) 100%); }
  .back-cover .texture {
    position: absolute; left: 120px; top: 250px; width: 420px; height: 360px;
    background: radial-gradient(ellipse at 50% 50%, rgba(255,255,255,0.10), rgba(255,255,255,0) 70%);
  }
  .back-content { position: absolute; left: 38px; top: 104px; width: 480px; }
  .back-content h2 { font-size: 14px; font-weight: 700; margin: 0 0 6px; }
  .back-content p { font-size: 10px; line-height: 1.6; color: var(--text-soft); margin-bottom: 18px; }
  .references p { margin-bottom: 10px; }

  .back-footer { position: absolute; left: 0; bottom: 0; width: 558px; height: 240px; }
  .footer-band { position: absolute; left: 0; top: 0; }
  .office { position: absolute; top: 80px; font-size: 9.5px; line-height: 1.5; color: var(--text-soft); }
  .office h3 { font-size: 12px; font-weight: 400; letter-spacing: 0.3px; color: var(--white); margin-bottom: 8px; }
  .office .row { display: flex; gap: 6px; align-items: flex-start; }
  .office .row .icon { margin-top: 3px; }
  .office-uk { left: 38px; }
  .office-asia { left: 215px; }
  .connect { position: absolute; left: 390px; top: 80px; font-size: 9.5px; color: var(--text-soft); }
  .social { display: flex; gap: 6px; margin-bottom: 12px; }
  .social span { width: 16px; height: 16px; border-radius: 50%; background: var(--blue-light); display: block; }
  .connect .row { display: flex; gap: 6px; align-items: center; }
  .back-url { position: absolute; left: 60px; bottom: 12px; font-size: 15px; display: flex; align-items: center; gap: 8px; }

  /* Front cover */
  .front-cover { background: var(--navy); }
  .cover-photo {
    position: absolute; left: 0; top: 0; width: 558px; height: 620px;
    background:
      linear-gradient(180deg, rgba(236,234,246,0.55) 0%, rgba(255,255,255,0) 40%),
      linear-gradient(110deg, #f3f1f6 0%, #dcd8e4 35%, #b9b2c4 60%, #8f8fa3 80%, #6d7894 100%);
  }
  .logo-tab { position: absolute; left: 250px; top: 0; width: 190px; height: 120px; }
  .logo-tab .tab-shape { position: absolute; left: 0; top: 0; }
  .logo-mark { position: absolute; left: 0; right: 0; top: 40px; display: flex; justify-content: center; align-items: center; gap: 7px; }
  .logo-mark .dot { width: 12px; height: 12px; background: var(--logo-blue); display: block; }
  .logo-mark .name { font-size: 19px; font-weight: 700; color: var(--logo-blue); letter-spacing: 0.2px; }
  .front-footer { position: absolute; left: 0; bottom: 0; width: 558px; height: 260px; }
  .cover-title { position: absolute; right: 38px; top: 80px; text-align: right; font-weight: 300; font-size: 25px; line-height: 1.35; }
  .front-url { position: absolute; right: 48px; bottom: 18px; font-size: 14px; display: flex; align-items: center; gap: 8px; }
</style>
</head>
<body>
<main class="spread">

  <section class="page back-cover" aria-label="Back cover">
    <div class="texture" role="img" aria-label="Faint aerial photograph of a ship at sea"></div>

    <div class="back-content">
      <h2>The Future Of Telemedicine</h2>
      <p>Telemedicine has developed over the years and continues to evolve today. Lightweight portable ultrasound devices are being developed, not just for producing images, but with treatment capabilities. The pioneering technology uses high-density ultrasound waves to stop internal bleeding, for example from deep tissue and from internal organs. This could enable a larger proportion of patients at sea to be treated in situ, without the need to be transported to a hospital. The Continental Space Agency (CSA) is helping to fund research into the development of robots which could perform medical procedures, such as scans and even surgical operations when controlled remotely by a medical professional.</p>

      <h2>Conclusion</h2>
      <p>In the meantime, making use of the telemedicine services available offers the best opportunity for optimising crew welfare and ensuring compliance with the requirements of the Maritime Labour Convention, to provide healthcare of a standard as close as possible to that provided ashore. It also enables ship owners to keep emergency medical costs to a minimum. This combined with a high level of medical competence in nominated officers, through regular high quality training, will help to deliver greater levels of self sufficiency for managing illness and injury at sea.</p>

      <div class="references">
        <h2>References</h2>
        <p>Maritime Labour Convention<br>http://www.labour-standards.example/public/normes/documents/instrument/mlc_2006.pdf</p>
        <p>Harrowgate Advisory report: Securing Skilled Crews in Today's Marketplace.</p>
        <p>Keelmark Register</p>
        <p>MedArchive article: Nautical officers at sea: emergency experience and need for medical training (2014)</p>
      </div>
    </div>

    <footer class="back-footer">
      <svg class="footer-band" width="558" height="240" viewBox="0 0 558 240" aria-hidden="true">
        <path d="M0 62 Q280 40 558 12 L558 240 L0 240 Z" fill="var(--navy)"/>
        <path d="M0 206 Q280 194 558 172 L558 240 L0 240 Z" fill="var(--blue-light)"/>
      </svg>

      <div class="office office-uk">
        <h3>UK HEAD OFFICE</h3>
        <div class="row">
          <svg class="icon" width="8" height="10" viewBox="0 0 8 10" aria-hidden="true"><path d="M4 0a3.5 3.5 0 0 0-3.5 3.5C.5 6 4 10 4 10s3.5-4 3.5-6.5A3.5 3.5 0 0 0 4 0zm0 5a1.4 1.4 0 1 1 0-2.8A1.4 1.4 0 0 1 4 5z" fill="#fff"/></svg>
          <span>14 Harbour Lane, Kelsby Quay,<br>Northfleet,<br>NF2 7QD</span>
        </div>
        <div class="row">
          <svg class="icon" width="9" height="9" viewBox="0 0 10 10" aria-hidden="true"><circle cx="5" cy="5" r="4.3" fill="none" stroke="#fff" stroke-width="1"/><path d="M3.3 2.8l1 1-0.5.7c.4.8.9 1.3 1.7 1.7l.7-.5 1 1-.8.8C4.8 7.3 2.7 5.2 2.5 3.6z" fill="#fff"/></svg>
          <span>+44 (0)1632 960 418</span>
        </div>
        <div class="row">
          <svg class="icon" width="9" height="9" viewBox="0 0 10 10" aria-hidden="true"><rect x="2" y="0.5" width="6" height="3" fill="#fff"/><rect x="0.5" y="3.5" width="9" height="4" rx="1" fill="#fff"/><rect x="2" y="6.5" width="6" height="3" fill="#fff"/></svg>
          <span>+44 (0)1632 960 519</span>
        </div>
      </div>

      <div class="office office-asia">
        <h3>ASIA OFFICE</h3>
        <div class="row">
          <svg class="icon" width="8" height="10" viewBox="0 0 8 10" aria-hidden="true"><path d="M4 0a3.5 3.5 0 0 0-3.5 3.5C.5 6 4 10 4 10s3.5-4 3.5-6.5A3.5 3.5 0 0 0 4 0zm0 5a1.4 1.4 0 1 1 0-2.8A1.4 1.4 0 0 1 4 5z" fill="#fff"/></svg>
          <span>9 Marina Walk<br>Level 5 Tidegate Tower<br>Singapore 000000</span>
        </div>
        <div class="row">
          <svg class="icon" width="9" height="9" viewBox="0 0 10 10" aria-hidden="true"><circle cx="5" cy="5" r="4.3" fill="none" stroke="#fff" stroke-width="1"/><path d="M3.3 2.8l1 1-0.5.7c.4.8.9 1.3 1.7 1.7l.7-.5 1 1-.8.8C4.8 7.3 2.7 5.2 2.5 3.6z" fill="#fff"/></svg>
          <span>+65 6000 1290</span>
        </div>
      </div>

      <div class="connect">
        <div class="social" aria-label="Social channels"><span></span><span></span><span></span><span></span></div>
        <div class="row">
          <svg class="icon" width="11" height="8" viewBox="0 0 11 8" aria-hidden="true"><rect x="0.5" y="0.5" width="10" height="7" fill="none" stroke="#fff"/><path d="M0.5 0.5l5 4 5-4" fill="none" stroke="#fff"/></svg>
          <span>info@sorvind-nautic.example</span>
        </div>
      </div>

      <div class="back-url">
        <svg class="icon" width="13" height="13" viewBox="0 0 14 14" aria-hidden="true"><circle cx="7" cy="7" r="6" fill="none" stroke="#fff" stroke-width="1.2"/><ellipse cx="7" cy="7" rx="2.6" ry="6" fill="none" stroke="#fff" stroke-width="1"/><path d="M1 7h12" stroke="#fff" stroke-width="1"/></svg>
        <span>www.sorvind-nautic.example</span>
      </div>
    </footer>
  </section>

  <section class="page front-cover" aria-label="Front cover">
    <div class="cover-photo" role="img" aria-label="Photograph of a clinician's hand using a tablet beside a bridge navigation console, with stacked shipping containers and sky behind"></div>

    <div class="logo-tab">
      <svg class="tab-shape" width="190" height="120" viewBox="0 0 190 120" aria-hidden="true">
        <path d="M0 0 H190 V95 L95 120 L0 95 Z" fill="var(--white)"/>
      </svg>
      <div class="logo-mark">
        <span class="dot"></span>
        <span class="name">Sorvind Nautic</span>
      </div>
    </div>

    <footer class="front-footer">
      <svg class="footer-band" width="558" height="260" viewBox="0 0 558 260" aria-hidden="true">
        <path d="M0 90 Q300 40 558 10 L558 260 L0 260 Z" fill="var(--navy)"/>
        <path d="M0 228 Q300 200 558 160 L558 260 L0 260 Z" fill="var(--blue-light)"/>
      </svg>
      <h1 class="cover-title">Telemedicine<br>for the Marine Industry</h1>
      <div class="front-url">
        <svg class="icon" width="13" height="13" viewBox="0 0 14 14" aria-hidden="true"><circle cx="7" cy="7" r="6" fill="none" stroke="#fff" stroke-width="1.2"/><ellipse cx="7" cy="7" rx="2.6" ry="6" fill="none" stroke="#fff" stroke-width="1"/><path d="M1 7h12" stroke="#fff" stroke-width="1"/></svg>
        <span>www.sorvind-nautic.example</span>
      </div>
    </footer>
  </section>

</main>
</body>
</html>
```